PaceHarbor

This involves designing the UI for an app used for training with others. The app will give the user a lists of sports they can create events on. The pace harbor logo design should be quite prominent in the app ui design. I have uploaded a sample. And also pictures of my attempt at designing this. I would like this design enhanced for android and ios. the sports being offered are as follows.

Running
Long Distance -
Middle distance -
Sprint -

Cycling
Spinning -
Mountain biking - just the same image places at an angle with a line underneath
Road - maybe with the road laid out below
Sprint - with lines to indicate speed maybe

Gym -
Weightlifting
Forgeloop
Yoga -
Palates -

Combat -
Boxing
BJJ
Kickboxing
Wrestling

Water Sports -
Swimming -
Water polo -
Kayaking -

Games -
Basketball
Football
Golf -
Badmington -

Walking - -
Hiking -
City Walking -

Cover art.

Industry/Entity Type

Health And Wellness

Number of Pages Required

1 page

Requirements
Must have
• Android and iOS design

```html
<!DOCTYPE html>
<html lang="en">
<head>
<meta charset="utf-8">
<title>PaceHarbor – App UI</title>
<link rel="stylesheet" href="https://fonts.googleapis.com/css2?family=Source+Sans+3:wght@400;600;700;900&display=swap">
<style>
:root{
  --page:#e1e1e6;
  --blue:#1a86d6;
  --blue-deep:#1670b8;
  --green:#0fc455;
  --red:#cc1414;
  --friend:#4b5da6;
  --field:#e6e6ea;
  --white:#ffffff;
  --ink:#444;
  --muted:#9a9aa2;
  --accent:#f5a30a;
  --sport-red:#e8194a;
  --sport-orange:#f39512;
  --sport-green:#4db51b;
  --sport-blue:#1fa6ef;
}
*{box-sizing:border-box;margin:0;padding:0}
html,body{width:1200px;height:960px;overflow:hidden;background:var(--page)}
body{font-family:"Source Sans 3",Arial,sans-serif;color:var(--white)}
.board{position:absolute;left:0;top:0;width:1082px;height:866px;transform:scale(1.109);transform-origin:0 0}
.screen{position:absolute;width:232px;height:412px;background:var(--blue);overflow:hidden}
.screen .figure{position:absolute;left:50px;top:60px;width:140px;height:360px;border-radius:70px 70px 30px 30px;background:radial-gradient(ellipse at center,rgba(20,90,150,.35),rgba(20,90,150,0) 70%)}
.status{position:absolute;left:0;top:0;width:100%;height:14px;font-size:8px;font-weight:600}
.status .dots{position:absolute;left:4px;top:3px;letter-spacing:-1px;font-size:7px}
.status .time{position:absolute;left:0;right:0;text-align:center;top:2px}
.status .battery{position:absolute;right:6px;top:4px;width:16px;height:7px;background:var(--white);border-radius:1px}
.abs{position:absolute}
.wordmark{position:absolute;left:0;right:0;text-align:center;font-weight:900;font-size:40px;letter-spacing:-1px;color:var(--white)}
.field{position:absolute;left:14px;width:204px;height:33px;background:var(--white);color:#333;font-size:11px;display:flex;align-items:center;justify-content:center;border:1px solid #ddd}
.btn{position:absolute;left:14px;width:204px;height:32px;font-size:11.5px;display:flex;align-items:center;justify-content:center;color:var(--white)}
.btn.green{background:var(--green)}
.btn.red{background:var(--red)}
.btn.friend{background:var(--friend)}
.tile{position:absolute;border-radius:9px;border:1px solid rgba(255,255,255,.35)}
.tile.red{background:linear-gradient(#f23a65,var(--sport-red))}
.tile.orange{background:linear-gradient(#fbae3a,var(--sport-orange))}
.tile.green{background:linear-gradient(#71cc36,var(--sport-green))}
.tile.blue{background:linear-gradient(#4cbcf7,var(--sport-blue))}
.avatar{position:absolute;border-radius:50%;background:radial-gradient(circle at 50% 45%,#6b4a36 0 34%,#e8e8e8 35%);border:3px solid #f2f2f2}
.label{position:absolute;font-size:11px}
.bold{font-weight:700;font-size:11.5px}
.toggle{position:absolute;left:14px;top:128px;width:204px;height:20px;display:flex;font-size:11px}
.toggle span{flex:1;display:flex;align-items:center;justify-content:center}
.toggle .on{background:var(--green)}
.toggle .off{background:var(--field);color:var(--ink)}
.box{position:absolute;background:var(--field);border:1px solid #cfcfd4}
.select{color:var(--muted);font-size:11px;padding-left:8px;display:flex;align-items:center}
.select svg{position:absolute;right:6px;top:6px}
.slider{position:absolute;width:104px;height:6px;background:#eaeaea;border-radius:3px}
.slider .fill{position:absolute;left:0;top:0;height:6px;background:var(--green);border-radius:3px}
.slider .knob{position:absolute;top:-10px;width:26px;height:26px;border-radius:50%;background:#f0f0f0;border:1px solid #ccc;color:var(--muted);font-size:10px;display:flex;align-items:center;justify-content:center}
.bar{position:absolute;height:20px;background:var(--field);color:var(--ink);font-size:11px;display:flex;align-items:center;justify-content:center;border:1px solid #cfcfd4}
.tabs svg{position:absolute;top:378px}
</style>
</head>
<body>
<svg width="0" height="0" style="position:absolute">
  <defs>
    <symbol id="i-person" viewBox="0 0 24 24"><circle cx="12" cy="7" r="5"/><path d="M2 23c0-6 4-9 10-9s10 3 10 9z"/></symbol>
    <symbol id="i-group" viewBox="0 0 28 24"><circle cx="10" cy="7" r="5"/><path d="M0 23c0-6 4-9 10-9s10 3 10 9z"/><circle cx="19" cy="6" r="4.5"/><path d="M21 13c4 0 7 3 7 9h-6c0-4-1-7-3-9z"/></symbol>
    <symbol id="i-cal" viewBox="0 0 24 24"><rect x="2" y="4" width="20" height="19" rx="2" fill="none" stroke="currentColor" stroke-width="2"/><rect x="2" y="4" width="20" height="5"/><rect x="6" y="1" width="2" height="5"/><rect x="16" y="1" width="2" height="5"/><text x="12" y="20" font-size="9" font-weight="700" text-anchor="middle" font-family="Source Sans 3,sans-serif">17</text></symbol>
  </defs>
</svg>

<main class="board">

  <!-- Login -->
  <section class="screen" style="left:14px;top:14px">
    <div class="figure" role="img" aria-label="faint athlete silhouette"></div>
    <div class="status"><span class="dots">●●●●●</span><span class="time">9:00 AM</span><span class="battery"></span></div>
    <div class="wordmark" style="top:58px">PaceHarbor</div>
    <div class="field" style="top:157px">Username</div>
    <div class="field" style="top:190px">************</div>
    <div class="btn green" style="top:230px">Login</div>
    <div class="label" style="left:0;right:0;text-align:center;top:265px;font-size:9px">- or -</div>
    <div class="btn friend" style="top:280px">Log in with Friendlink</div>
    <div class="label" style="left:0;right:0;text-align:center;top:377px">Recover password?</div>
  </section>

  <!-- Sport picker -->
  <section class="screen" style="left:285px;top:14px">
    <div class="figure" role="img" aria-label="faint athlete silhouette"></div>
    <div class="status"><span class="dots">●●●●●</span><span class="time">9:00 AM</span><span class="battery"></span></div>
    <div class="wordmark" style="top:58px">PaceHarbor</div>
    <div class="tile red" style="left:45px;top:156px;width:71px;height:71px" role="img" aria-label="cycling sport icon"></div>
    <div class="tile orange" style="left:119px;top:156px;width:71px;height:71px" role="img" aria-label="wrestling sport icon"></div>
    <div class="tile green" style="left:45px;top:229px;width:71px;height:71px" role="img" aria-label="running sport icon"></div>
    <div class="tile blue" style="left:119px;top:229px;width:71px;height:71px" role="img" aria-label="boxing sport icon"></div>
    <div class="tabs">
      <svg style="left:13px" width="24" height="24" fill="#fff"><use href="#i-person"/></svg>
      <svg style="left:104px;color:var(--accent)" width="24" height="24" fill="var(--accent)"><use href="#i-cal"/></svg>
      <svg style="left:190px" width="28" height="24" fill="#fff"><use href="#i-group"/></svg>
    </div>
  </section>

  <!-- Create event -->
  <section class="screen" style="left:561px;top:14px">
    <div class="figure" role="img" aria-label="faint athlete silhouette"></div>
    <div class="status"><span class="dots">●●●●●</span><span class="time">9:00 AM</span><span class="battery"></span></div>
    <div class="avatar" style="left:21px;top:42px;width:70px;height:70px" role="img" aria-label="user profile photo"></div>
    <div class="tile red" style="left:155px;top:43px;width:44px;height:44px" role="img" aria-label="spinning sport icon"></div>
    <div class="label" style="left:124px;width:100px;text-align:center;top:95px">Type: Spinning</div>
    <div class="toggle"><span class="on">Private</span><span class="off">Public</span></div>
    <div class="label" style="left:19px;top:167px">Time</div>
    <div class="box select" style="left:115px;top:159px;width:103px;height:32px">12:00
      <svg width="12" height="20" viewBox="0 0 12 20"><path d="M6 1l5 7H1z M6 19l5-7H1z" fill="#1a6fc4"/></svg>
    </div>
    <div class="label" style="left:19px;top:204px">Distance</div>
    <div class="slider" style="left:114px;top:209px"><span class="fill" style="width:53px"></span><span class="knob" style="left:40px">10 k</span></div>
    <div class="label" style="left:19px;top:238px;line-height:13px">Number of Parti-<br>cipants</div>
    <div class="slider" style="left:114px;top:251px"><span class="fill" style="width:47px"></span><span class="knob" style="left:34px">9</span></div>
    <div class="label" style="left:19px;top:289px">Location</div>
    <div class="box" style="left:115px;top:279px;width:103px;height:32px"></div>
    <div class="btn green" style="top:328px">Create Event</div>
    <div class="tabs">
      <svg style="left:13px" width="24" height="24" fill="#fff"><use href="#i-person"/></svg>
      <svg style="left:104px;color:var(--accent)" width="24" height="24" fill="var(--accent)"><use href="#i-cal"/></svg>
      <svg style="left:190px" width="28" height="24" fill="#fff"><use href="#i-group"/></svg>
    </div>
  </section>

  <!-- Invitation -->
  <section class="screen" style="left:833px;top:14px">
    <div class="figure" role="img" aria-label="faint athlete silhouette"></div>
    <div class="status"><span class="dots">●●●●●</span><span class="time">9:00 AM</span><span class="battery"></span></div>
    <div class="btn green" style="top:54px">Accept</div>
    <div class="avatar" style="left:38px;top:113px;width:102px;height:102px" role="img" aria-label="user profile photo"></div>
    <div class="label bold" style="left:169px;top:134px">John</div>
    <div class="label bold" style="left:169px;top:178px">36</div>
    <div class="tile red" style="left:15px;top:238px;width:44px;height:44px" role="img" aria-label="cycling sport icon"></div>
    <div class="tile blue" style="left:68px;top:238px;width:44px;height:44px" role="img" aria-label="boxing sport icon"></div>
    <div class="tile green" style="left:121px;top:238px;width:44px;height:44px" role="img" aria-label="running sport icon"></div>
    <div class="tile orange" style="left:174px;top:238px;width:44px;height:44px" role="img" aria-label="wrestling sport icon"></div>
    <div class="btn red" style="top:311px">Decline</div>
    <div class="tabs">
      <svg style="left:13px" width="24" height="24" fill="#fff"><use href="#i-person"/></svg>
      <svg style="left:104px;color:#fff" width="24" height="24" fill="#fff"><use href="#i-cal"/></svg>
      <svg style="left:190px" width="28" height="24" fill="var(--accent)"><use href="#i-group"/></svg>
    </div>
  </section>

  <!-- Hobbies -->
  <section class="screen" style="left:14px;top:443px">
    <div class="figure" role="img" aria-label="faint athlete silhouette"></div>
    <div class="status"><span class="dots">●●●●●</span><span class="time">9:00 AM</span><span class="battery"></span></div>
    <div class="avatar" style="left:38px;top:43px;width:102px;height:102px" role="img" aria-label="user profile photo"></div>
    <div class="label bold" style="left:168px;top:64px">John</div>
    <div class="label bold" style="left:168px;top:108px">36</div>
    <div class="bar" style="left:27px;top:160px;width:182px">Choose your hobbies</div>
    <div class="box" style="left:27px;top:194px;width:181px;height:151px"></div>
    <div class="tabs">
      <svg style="left:13px" width="24" height="24" fill="var(--accent)"><use href="#i-person"/></svg>
      <svg style="left:104px;color:#fff" width="24" height="24" fill="#fff"><use href="#i-cal"/></svg>
      <svg style="left:190px" width="28" height="24" fill="#fff"><use href="#i-group"/></svg>
    </div>
  </section>

  <!-- Preferences -->
  <section class="screen" style="left:285px;top:443px">
    <div class="figure" role="img" aria-label="faint athlete silhouette"></div>
    <div class="status"><span class="dots">●●●●●</span><span class="time">9:00 AM</span><span class="battery"></span></div>
    <div class="avatar" style="left:36px;top:43px;width:102px;height:102px" role="img" aria-label="user profile photo"></div>
    <div class="label bold" style="left:168px;top:64px">John</div>
    <div class="label bold" style="left:168px;top:108px">36</div>
    <div class="bar" style="left:26px;top:160px;width:182px">Preferences</div>
    <div class="label" style="left:28px;top:199px">Distance</div>
    <div class="slider" style="left:105px;top:205px"><span class="fill" style="width:47px"></span><span class="knob" style="left:34px">9</span></div>
    <div class="tabs">
      <svg style="left:13px" width="24" height="24" fill="var(--accent)"><use href="#i-person"/></svg>
      <svg style="left:104px;color:#fff" width="24" height="24" fill="#fff"><use href="#i-cal"/></svg>
      <svg style="left:190px" width="28" height="24" fill="#fff"><use href="#i-group"/></svg>
    </div>
  </section>

</main>
</body>
</html>
```